Bref créative |
BrightMoor Guard, LLC. | ||
Use standard fonts | ||
Cutting-Edge Modern Simple |
Derek Palvane | ||
Master Technician | ||
leave blank | ||
brightmooritllc@quellmail.example | ||
http://brightmoorguard.example | ||

```html
<!DOCTYPE html>
<html lang="en">
<head>
<meta charset="utf-8">
<title>BrightMoor Guard, LLC. — Business Card</title>
<link rel="stylesheet" href="https://fonts.googleapis.com/css2?family=Cinzel:wght@400;600&display=swap">
<style>
  :root {
    --bg: #e4e5e7;
    --blue-light: #3f86d8;
    --blue: #1f63bf;
    --blue-deep: #154a98;
    --white: #ffffff;
    --ink: #1d2f57;
    --swoosh: #111418;
    --card-shadow: rgba(0, 0, 0, 0.18);
  }
  * { box-sizing: border-box; margin: 0; padding: 0; }
  html, body { width: 1200px; height: 904px; overflow: hidden; }
  body {
    background: var(--bg);
    font-family: "Cinzel", "Times New Roman", serif;
    position: relative;
  }
  .card {
    position: absolute;
    width: 540px;
    height: 308px;
    border-radius: 4px;
    overflow: hidden;
    box-shadow: 0 6px 18px var(--card-shadow);
  }
  /* Contact side */
  .card--contact { left: 40px; top: 298px; background: var(--white); }
  .card--contact .card__shape { position: absolute; inset: 0; }
  .contact {
    position: absolute;
    left: 22px; top: 36px;
    color: var(--white);
  }
  .contact__name { font-size: 18px; font-weight: 400; letter-spacing: 0.4px; white-space: nowrap; }
  .contact__title { font-size: 9px; letter-spacing: 1.1px; margin-top: 4px; opacity: 0.9; white-space: nowrap; }
  .contact__list { list-style: none; margin-top: 34px; }
  .contact__item {
    display: flex; align-items: center; gap: 6px;
    font-size: 7.5px; letter-spacing: 0; margin-bottom: 8px;
    white-space: nowrap;
  }
  .contact__icon {
    flex: none;
    width: 12px; height: 12px; border-radius: 50%;
    background: var(--white);
    display: flex; align-items: center; justify-content: center;
  }
  .brand {
    position: absolute;
    left: 286px; top: 112px; width: 244px;
    text-align: center; color: var(--ink);
  }
  .brand__dot {
    width: 52px; height: 52px; border-radius: 50%;
    margin: 0 auto 10px;
    background: radial-gradient(circle at 35% 30%, var(--blue-light), var(--blue-deep));
  }
  .brand__name { font-size: 15px; font-weight: 600; white-space: nowrap; }
  .brand__tagline { font-size: 9px; letter-spacing: 1.2px; margin-top: 3px; white-space: nowrap; }

  /* Blue side */
  .card--cover {
    left: 620px; top: 298px;
    background: linear-gradient(160deg, var(--blue-light) 0%, var(--blue) 55%, var(--blue-deep) 100%);
  }
  .cover__mark {
    position: absolute; left: 120px; top: -40px;
    width: 190px; height: 190px; border-radius: 50%;
    background: rgba(255, 255, 255, 0.07);
  }
  .cover__text {
    position: absolute; right: 44px; top: 150px;
    color: var(--white); text-align: center;
  }
  .cover__name { font-size: 22px; font-weight: 400; letter-spacing: 0.5px; white-space: nowrap; }
  .cover__tagline { font-size: 12px; letter-spacing: 1.5px; margin-top: 2px; white-space: nowrap; }
</style>
</head>
<body>

  <section class="card card--contact">
    <svg class="card__shape" width="540" height="308" viewBox="0 0 540 308" aria-hidden="true">
      <defs>
        <linearGradient id="panelBlue" x1="0" y1="0" x2="1" y2="1">
          <stop offset="0" stop-color="#3f86d8"/>
          <stop offset="1" stop-color="#1a58ad"/>
        </linearGradient>
      </defs>
      <path d="M0 0 H300 C255 70 250 230 272 308 H0 Z" fill="url(#panelBlue)"/>
      <path d="M300 0 C255 70 250 230 272 308 L286 308 C265 230 271 70 315 0 Z" fill="#111418"/>
    </svg>

    <div class="contact">
      <h1 class="contact__name">Derek Palvane</h1>
      <p class="contact__title">Master Technician</p>
      <ul class="contact__list">
        <li class="contact__item">
          <span class="contact__icon">
            <svg width="7" height="7" viewBox="0 0 10 10"><path d="M2 1 L4 1 L4.6 3 L3.5 3.8 C4 5 5 6 6.2 6.5 L7 5.4 L9 6 L9 8 C5 9 1 5 2 1 Z" fill="#1f63bf"/></svg>
          </span>(555) 014-2286
        </li>
        <li class="contact__item">
          <span class="contact__icon">
            <svg width="7" height="7" viewBox="0 0 10 10"><rect x="1" y="2.5" width="8" height="5.5" fill="none" stroke="#1f63bf" stroke-width="1.2"/><path d="M1 2.5 L5 6 L9 2.5" fill="none" stroke="#1f63bf" stroke-width="1.2"/></svg>
          </span>brightmooritllc@quellmail.example
        </li>
        <li class="contact__item">
          <span class="contact__icon">
            <svg width="7" height="7" viewBox="0 0 10 10"><circle cx="5" cy="5" r="4" fill="none" stroke="#1f63bf" stroke-width="1.1"/><path d="M1 5 H9 M5 1 C3 3.5 3 6.5 5 9 M5 1 C7 3.5 7 6.5 5 9" fill="none" stroke="#1f63bf" stroke-width="0.9"/></svg>
          </span>http://brightmoorguard.example
        </li>
      </ul>
    </div>

    <div class="brand">
      <div class="brand__dot"></div>
      <p class="brand__name">BrightMoor Guard, LLC.</p>
      <p class="brand__tagline">An IT Solutions Firm.</p>
    </div>
  </section>

  <section class="card card--cover">
    <div class="cover__mark"></div>
    <div class="cover__text">
      <p class="cover__name">BRIGHTMOOR GUARD, LLC.</p>
      <p class="cover__tagline">AN IT SOLUTIONS FIRM.</p>
    </div>
  </section>

</body>
</html>
```